Minimalist Modern Business Card Design, open to ideas, or cleaner version of provided files, but what logo & logo colors (with some black) as shown in files, and info for back shown in files as well.

```html
<!DOCTYPE html>
<html lang="en">
<head>
<meta charset="UTF-8">
<title>Roadway Rig Works – Business Card</title>
<link href="https://fonts.googleapis.com/css2?family=Montserrat:wght@400;600;800&family=Roboto+Condensed:wght@700&display=swap" rel="stylesheet">
<style>
  :root {
    --navy: #262262;
    --navy-deep: #2b3566;
    --slate: #6e7799;
    --amber: #f9a21b;
    --white: #ffffff;
    --ink: #111111;
    --stage: #ece8e1;
  }
  * { box-sizing: border-box; margin: 0; padding: 0; }
  html, body { width: 1200px; height: 675px; overflow: hidden; }
  body {
    background: var(--stage);
    position: relative;
    font-family: "Montserrat", Arial, sans-serif;
  }
  .card {
    position: absolute;
    top: 182px;
    width: 540px;
    height: 310px;
    border-radius: 26px;
    overflow: hidden;
    box-shadow: 0 10px 24px rgba(0,0,0,0.18);
  }

  /* Back side */
  .card-back {
    left: 40px;
    background: var(--navy);
    color: var(--white);
    font-family: "Roboto Condensed", "Arial Narrow", sans-serif;
    font-weight: 700;
    display: flex;
    gap: 30px;
    padding: 30px 34px;
  }
  .list-block { display: flex; flex-direction: column; }
  .list-block.services { width: 280px; }
  .pill {
    align-self: flex-start;
    background: var(--amber);
    color: var(--ink);
    font-size: 15px;
    letter-spacing: 0.2px;
    padding: 5px 16px;
    border-radius: 16px;
    margin-bottom: 10px;
  }
  .bullets { list-style: none; }
  .bullets li {
    font-size: 14.5px;
    line-height: 20.5px;
    padding-left: 16px;
    position: relative;
    white-space: nowrap;
  }
  .bullets li::before {
    content: "";
    position: absolute;
    left: 2px; top: 8px;
    width: 5px; height: 5px;
    border-radius: 50%;
    background: var(--white);
  }

  /* Front side */
  .card-front {
    left: 620px;
    background: var(--white);
    color: var(--navy);
  }
  .corner-bands { position: absolute; left: 0; top: 0; }
  .brand-top {
    position: absolute;
    top: 30px; right: 40px;
    display: flex; align-items: center; gap: 10px;
  }
  .brand-mark {
    width: 14px; height: 14px;
    background: var(--navy);
  }
  .brand-top .brand-name {
    font-size: 20px; font-weight: 600; line-height: 1.05;
  }
  .brand-feature {
    position: absolute;
    left: 38px; top: 110px;
    width: 190px;
    font-size: 30px; font-weight: 800; line-height: 1.08;
    color: var(--navy);
  }
  .divider {
    position: absolute;
    left: 236px; top: 100px;
    width: 1.5px; height: 150px;
    background: var(--navy);
  }
  .person { position: absolute; left: 256px; top: 108px; }
  .person-name { font-size: 33px; font-weight: 800; letter-spacing: 0.5px; line-height: 1; }
  .person-role { font-size: 17px; font-weight: 600; color: var(--ink); margin-top: 4px; }
  .contacts { position: absolute; left: 256px; top: 192px; }
  .contact {
    display: flex; align-items: center; gap: 8px;
    font-size: 14px; font-weight: 600; color: var(--ink);
    line-height: 24px;
    white-space: nowrap;
  }
  .website {
    position: absolute; left: 38px; bottom: 30px;
    font-size: 14px; font-weight: 600; color: var(--ink);
  }
</style>
</head>
<body>

<section class="card card-back" aria-label="Card back: services">
  <div class="list-block services">
    <span class="pill">SERVICES INCLUDE:</span>
    <ul class="bullets">
      <li>Shop &amp; Mobile</li>
      <li>DOT &amp; BIT Inspections</li>
      <li>All Maintenance &amp; Repairs</li>
      <li>Check Engine Lights</li>
      <li>Diags, Regens &amp; Programming</li>
      <li>Full Dealer Software Capabilities</li>
      <li>PM &amp; Compliance Tracking</li>
      <li>App-Based Billing &amp; Live Updates</li>
      <li>Dealer Certified Techs</li>
      <li>Night Servicing to Avoid Downtime</li>
    </ul>
  </div>
  <div class="list-block specialties">
    <span class="pill">SPECIALIZING IN:</span>
    <ul class="bullets">
      <li>Heavy &amp; Medium Duty</li>
      <li>Corvane</li>
      <li>Izora</li>
      <li>Hadro</li>
      <li>Petrovale</li>
      <li>Freightway</li>
      <li>Kenmark</li>
      <li>Alderson</li>
      <li>AfterTreatment</li>
      <li>And More</li>
    </ul>
  </div>
</section>

<section class="card card-front" aria-label="Card front: contact">
  <svg class="corner-bands" width="540" height="310" viewBox="0 0 540 310" aria-hidden="true">
    <polygon points="540,175 540,310 345,310" fill="var(--slate)"/>
    <polygon points="345,310 540,222 540,310" fill="var(--navy-deep)"/>
    <line x1="345" y1="310" x2="540" y2="217" stroke="var(--white)" stroke-width="5"/>
  </svg>

  <div class="brand-top">
    <span class="brand-mark"></span>
    <span class="brand-name">Roadway<br>Rig Works</span>
  </div>

  <div class="brand-feature">Roadway Rig Works</div>

  <div class="divider"></div>

  <div class="person">
    <div class="person-name">MY NAME</div>
    <div class="person-role">President</div>
  </div>

  <div class="contacts">
    <div class="contact">
      <svg width="16" height="16" viewBox="0 0 16 16" aria-hidden="true">
        <circle cx="8" cy="8" r="7" fill="none" stroke="var(--navy)" stroke-width="1.3"/>
        <rect x="5.5" y="3.8" width="5" height="8.4" rx="1" fill="none" stroke="var(--navy)" stroke-width="1.2"/>
      </svg>
      555 014 2786
    </div>
    <div class="contact">
      <svg width="16" height="16" viewBox="0 0 16 16" aria-hidden="true">
        <circle cx="8" cy="8" r="7" fill="none" stroke="var(--navy)" stroke-width="1.3"/>
        <rect x="4.2" y="5.3" width="7.6" height="5.4" fill="var(--navy)"/>
        <polyline points="4.2,5.3 8,8.3 11.8,5.3" fill="none" stroke="var(--white)" stroke-width="0.9"/>
      </svg>
      info@rigworksco.com
    </div>
  </div>

  <div class="website">www.rigworksco.com</div>
</section>

</body>
</html>
```